School Website

I need a design for a School (2 sections: Primary 6-12 years and Secondary 12-18 years). The first page is just a choice of the 2 sections. After we'll need 2 websites (with the same structure: Menu, ...) but with different colors. In fact, we need for end of October, 6 design of school website. So the best websites are going to be made available to you in the future (in pixmarketo) but privately.

Target Market(s)

Public, Parents, ...

Coding

Coded - Design and coding required

Number of Pages Required

5+ page

Font styles to use
Sans Serif

Colors
34a6d7
85cae6
cee9f5
ffffff

Requirements
Must have
• You can check the old Website: http: / /velmoq.be We need the same pages with the same content. Menu: - HomePage - News and communication (like blog page) - Activities (like blog page, with photo gallery) - Contact (Contact form + maps) - In the main menu, we need a special button to connect to an external Website ( button needs to be different than the other menu items The name of this button is "Parents Area"). The logo of 2 sections are attached. Please use it for the design and the choice of colors.
Nice to have
• This is a web design of other school that we like: https://www.quintel.be

```html
<!DOCTYPE html>
<html lang="en">
<head>
<meta charset="utf-8">
<title>Athénée Royal de Velmoq – Section Secondaire</title>
<link href="https://fonts.googleapis.com/css2?family=Poppins:wght@400;500;600;700;800&display=swap" rel="stylesheet">
<style>
:root{
  --blue:#1b75bf;
  --blue-dark:#1466ad;
  --blue-light:#3d8fd1;
  --orange:#d86f1a;
  --orange-light:#e8873a;
  --teal:#3fb4b0;
  --ink:#1f1f1f;
  --text:#3a3a3a;
  --muted:#666;
  --line:#d8dde3;
  --footer:#262626;
  --white:#fff;
}
*{margin:0;padding:0;box-sizing:border-box}
html,body{width:1200px;height:3743px;overflow:hidden}
body{position:relative;font-family:"Poppins",sans-serif;color:var(--text);background:var(--white)}
.abs{position:absolute}
a{color:inherit;text-decoration:none}

/* header */
.brand{left:87px;top:30px;display:flex;align-items:center;gap:10px;font-size:19px;font-weight:600;color:var(--blue-dark)}
.brand-dot{width:34px;height:34px;border-radius:50%;background:var(--blue)}
.nav{top:42px;left:431px;display:flex;font-size:13.5px;color:#444}
.nav a{position:absolute;white-space:nowrap}
.nav .active{color:var(--blue)}
.btn-parents{position:absolute;display:flex;align-items:center;justify-content:center;font-weight:600;font-size:13.5px;letter-spacing:.3px}
.btn-parents::before{content:"";position:absolute;inset:8px -6px -6px 0;background:var(--orange);z-index:0;clip-path:polygon(0 0,100% 0,96% 100%,0 100%)}
.btn-parents span{position:relative;z-index:1;width:100%;height:100%;display:flex;align-items:center;justify-content:center;clip-path:polygon(0 0,100% 0,97% 100%,3% 100%)}
.btn-parents.head{left:963px;top:26px;width:144px;height:50px;color:#fff}
.btn-parents.head span{background:var(--blue-dark)}

/* hero */
.hero{left:0;top:99px;width:1200px;height:546px;background:var(--blue);overflow:hidden}
.hero .shape{position:absolute;background:rgba(255,255,255,.07);border-radius:40px;transform:rotate(45deg)}
.hero .bubble{position:absolute;left:375px;top:157px;width:204px;height:204px;border-radius:50%;background:var(--blue-light);opacity:.55}
.hero-title{left:88px;top:180px;color:#fff;z-index:2;white-space:nowrap}
.hero-title .pre{font-size:38px;font-weight:600;letter-spacing:.5px;line-height:1}
.hero-title h1{font-size:54px;font-weight:800;line-height:1;margin-top:14px;letter-spacing:-.5px}
.hero-title .sub{font-size:21px;font-weight:500;margin-top:14px}
.btn-parents.hero-btn{left:90px;top:340px;width:144px;height:48px;color:var(--blue-dark);font-size:13px;z-index:2}
.btn-parents.hero-btn span{background:#fff}
.hero-photo{left:660px;top:30px;width:380px;height:516px;border-radius:190px 190px 0 0;background:linear-gradient(180deg,#e9d3c0 0%,#6d8fb7 45%,#3c6694 100%)}
.hero-mark{color:#fff;font-size:22px;font-weight:300}

/* section heads */
.sec-title{width:1200px;text-align:center;font-size:44px;font-weight:700;color:var(--ink);letter-spacing:.5px;line-height:1}
.divider{width:180px;height:16px;left:510px}
.sec-text{left:260px;width:680px;text-align:center;font-size:14px;line-height:25px;color:#333}

/* cards */
.card{top:933px;width:313px;height:319px;background:#fff;box-shadow:0 4px 22px rgba(0,0,0,.08);padding:49px 24px 0 26px;overflow:hidden}
.card .icon{width:78px;height:78px;border-radius:50%;display:flex;align-items:center;justify-content:center}
.card h3{font-size:20px;font-weight:500;color:var(--ink);margin-top:22px}
.card p{font-size:12.5px;line-height:21px;color:#444;margin-top:10px;white-space:nowrap}
.card .go{position:absolute;right:-6px;bottom:-6px;width:50px;height:44px;border-radius:24px 0 0 0;background:#eceef1;display:flex;align-items:center;justify-content:center;padding:0 4px 4px 0}
.card .go.on{background:var(--teal)}

/* rules */
.rules{left:0;top:1376px;width:1200px;height:411px;background:var(--orange)}
.rules-title{top:1458px;width:1200px;text-align:center;font-size:46px;font-weight:700;color:#fff;line-height:1}
.rule-row{left:396px;display:flex;align-items:center;gap:12px;color:#fff}
.rule-row p{font-size:14px;line-height:20px}
.rule-row a{font-weight:600;text-decoration:underline;font-size:15.5px}
.ring{border-radius:50%;background:var(--orange-light);display:flex;align-items:center;justify-content:center}
.ring .ph{border-radius:50%}
.dot-deco{border-radius:50%;background:var(--orange-light)}

/* gallery */
.tile{top:2102px;width:301px;height:262px;display:flex;align-items:flex-end;justify-content:center;padding-bottom:22px;color:#fff;font-size:22px;font-weight:700}
.tile .badge{position:absolute;left:19px;top:19px;width:44px;height:44px;border-radius:50%;display:flex;align-items:center;justify-content:center}

/* meals */
.meal-photo{left:0;top:2466px;width:513px;height:435px;background:linear-gradient(135deg,#8fb24a 0%,#c8452c 40%,#a8301f 65%,#e3d9c7 100%)}
.chat{left:437px;top:2419px;width:122px;height:122px;border-radius:50%;background:var(--orange);display:flex;align-items:center;justify-content:center}
.meal-title{left:606px;top:2574px;font-size:44px;font-weight:700;color:var(--ink);letter-spacing:.5px;line-height:1}
.meal-text{left:607px;top:2661px;width:460px;font-size:14px;line-height:26px;color:#333}
.arrow-btn{top:2842px;width:38px;height:38px;border-radius:50%;display:flex;align-items:center;justify-content:center}

/* contact */
.footer{left:0;top:3361px;width:1200px;height:382px;background:var(--footer)}
.form-card{left:275px;top:3109px;width:650px;height:388px;background:#fff;box-shadow:0 6px 26px rgba(0,0,0,.1)}
.field{height:44px;border:1px solid var(--line);font-size:12px;color:#666;padding:0 12px;display:flex;align-items:center}
.field.msg{align-items:flex-start;padding-top:10px;height:127px}
.btn-parents.submit{left:526px;top:3417px;width:145px;height:47px;color:#fff;font-size:13px}
.btn-parents.submit span{background:var(--blue-dark)}

/* footer info */
.info{top:3564px;display:flex;align-items:center;gap:20px;color:#fff}
.info .ic{width:72px;height:72px;border-radius:50%;background:var(--blue-dark);display:flex;align-items:center;justify-content:center;flex:none}
.info h4{font-size:16px;font-weight:600;letter-spacing:.3px}
.info p{font-size:13.5px;line-height:22px}
.foot-line{left:87px;top:3699px;width:1023px;height:1px;background:#4a4a4a}
.copy{left:87px;top:3713px;font-size:12.5px;color:#ddd}
.sitemap{left:1049px;top:3713px;font-size:12.5px;color:var(--blue-light);text-decoration:underline}
.totop{left:1136px;top:3649px;width:38px;height:38px;border-radius:50%;background:var(--blue-dark);display:flex;align-items:center;justify-content:center}
</style>
</head>
<body>

<!-- header -->
<div class="abs brand"><span class="brand-dot"></span>Athénée Royal de Velmoq</div>
<nav class="abs nav">
  <a class="active" style="left:0">HOME</a>
  <a style="left:85px">NEWS &amp; COMMUNICATION</a>
  <a style="left:309px">ACIVITIES</a>
  <a style="left:415px">CONTACT</a>
</nav>
<a class="btn-parents head"><span>PARENTS AREA</span></a>

<!-- hero -->
<section class="abs hero">
  <div class="shape" style="left:-60px;top:-40px;width:260px;height:260px"></div>
  <div class="shape" style="left:120px;top:430px;width:220px;height:220px"></div>
  <div class="shape" style="left:860px;top:-120px;width:420px;height:420px"></div>
  <div class="bubble"></div>
  <div class="abs hero-photo" role="img" aria-label="Smiling student with glasses holding a pencil and a stack of books"></div>
  <div class="abs hero-title">
    <div class="pre">ATHÉNÉE</div>
    <h1>ROYAL DE VELMOQ</h1>
    <div class="sub">SECTION SECONDAIRE</div>
  </div>
  <a class="btn-parents hero-btn"><span>PARENTS AREA</span></a>
  <div class="abs hero-mark" style="left:668px;top:30px">+</div>
  <svg class="abs" style="left:830px;top:46px" width="20" height="20"><circle cx="10" cy="10" r="7.5" fill="none" stroke="#fff" stroke-width="1.6"/></svg>
  <svg class="abs" style="left:903px;top:176px" width="20" height="20"><circle cx="10" cy="10" r="7.5" fill="none" stroke="#fff" stroke-width="1.6"/></svg>
  <svg class="abs" style="left:601px;top:243px" width="20" height="18"><path d="M10 2 L18 16 H2 Z" fill="none" stroke="#fff" stroke-width="1.6"/></svg>
</section>

<!-- intro -->
<h2 class="abs sec-title" style="top:729px">ROYAL DE VELMOQ</h2>
<svg class="abs divider" style="top:778px" viewBox="0 0 180 16"><line x1="0" y1="8" x2="72" y2="8" stroke="#1b75bf"/><line x1="108" y1="8" x2="180" y2="8" stroke="#1b75bf"/><circle cx="76" cy="8" r="2.5" fill="#1b75bf"/><circle cx="104" cy="8" r="2.5" fill="#1b75bf"/><circle cx="90" cy="8" r="6" fill="none" stroke="#1b75bf" stroke-width="1.5"/><circle cx="90" cy="8" r="3" fill="#1b75bf"/></svg>
<p class="abs sec-text" style="top:803px">Lorem ipsum dolor sit amet, consectetur adipiscing elit, sed do eiusmod tempor incididunt ut<br>labore et dolore magna aliqua. Quis ipsum suspendisse ultrices gravida. Risus commodo<br>viverra maecenas accumsan lacus vel facilisis.</p>

<article class="abs card" style="left:89px">
  <div class="icon" style="background:var(--blue-dark)">
    <svg width="42" height="42" viewBox="0 0 42 42" fill="none" stroke="#fff" stroke-width="1.8"><circle cx="15" cy="15" r="6"/><circle cx="28" cy="15" r="6"/><path d="M4 34c0-7 5-11 11-11s11 4 11 11z"/><path d="M22 23c2-1 4-1 6-1 6 0 10 4 10 11h-9"/></svg>
  </div>
  <h3>Our Teaching Team</h3>
  <p>Director of the fundamental section<br>Rue Gaston Lemarche, 1a - 4820 VELMOQ<br>081 / 47.36.58<br>Mrs Claire VANDORMAEL</p>
  <span class="go"><svg width="18" height="12"><path d="M1 6h15M11 1l5 5-5 5" fill="none" stroke="#333" stroke-width="1.5"/></svg></span>
</article>
<article class="abs card" style="left:443px">
  <div class="icon" style="background:var(--teal)">
    <svg width="42" height="42" viewBox="0 0 42 42" fill="none" stroke="#fff" stroke-width="1.8"><rect x="5" y="8" width="30" height="26" rx="2"/><line x1="5" y1="15" x2="35" y2="15"/><line x1="12" y1="5" x2="12" y2="11"/><line x1="28" y1="5" x2="28" y2="11"/><path d="M10 20h3M16 20h3M22 20h3M10 25h3M16 25h3M10 30h3"/><circle cx="30" cy="30" r="6" fill="#3fb4b0"/><path d="M27 30l2 2 4-4"/></svg>
  </div>
  <h3>Our schedules &amp; daycare</h3>
  <p>Director of the fundamental section<br>Rue Gaston Lemarche, 1a - 4820 VELMOQ<br>081 / 47.36.58<br>Mrs Claire VANDORMAEL</p>
  <span class="go on"><svg width="18" height="12"><path d="M1 6h15M11 1l5 5-5 5" fill="none" stroke="#fff" stroke-width="1.5"/></svg></span>
</article>
<article class="abs card" style="left:795px">
  <div class="icon" style="background:var(--orange)">
    <svg width="42" height="42" viewBox="0 0 42 42" fill="none" stroke="#fff" stroke-width="1.8"><path d="M6 36V20h30v16z"/><path d="M13 20v-6l8-6 8 6v6"/><path d="M21 8V3h5v3h-5"/><rect x="18" y="27" width="6" height="9"/><rect x="9" y="24" width="4" height="4"/><rect x="29" y="24" width="4" height="4"/><circle cx="21" cy="16" r="2"/></svg>
  </div>
  <h3>School Holidays</h3>
  <p>Director of the fundamental section<br>Rue Gaston Lemarche, 1a - 4820 VELMOQ<br>081 / 47.36.58<br>Mrs Claire VANDORMAEL</p>
  <span class="go"><svg width="18" height="12"><path d="M1 6h15M11 1l5 5-5 5" fill="none" stroke="#333" stroke-width="1.5"/></svg></span>
</article>

<!-- rules of procedure -->
<section class="abs rules"></section>
<div class="abs dot-deco" style="left:-48px;top:1597px;width:96px;height:96px"></div>
<div class="abs dot-deco" style="left:1044px;top:1738px;width:92px;height:92px"></div>
<div class="abs ring" style="left:157px;top:1429px;width:130px;height:130px"><div class="ph" role="img" aria-label="Student with backpack giving a thumbs up" style="width:100px;height:100px;background:linear-gradient(160deg,#c9d3dc,#e9a441)"></div></div>
<div class="abs ring" style="left:940px;top:1426px;width:162px;height:162px"><div class="ph" role="img" aria-label="Students studying at desks in a classroom" style="width:132px;height:132px;background:linear-gradient(160deg,#e6e2dc,#8e4a3a)"></div></div>
<div class="abs ring" style="left:798px;top:1603px;width:116px;height:116px"><div class="ph" role="img" aria-label="Student holding notebooks" style="width:88px;height:88px;background:linear-gradient(160deg,#cfe0ef,#5f7d9c)"></div></div>
<div class="abs ring" style="left:173px;top:1647px;width:230px;height:230px"><div class="ph" role="img" aria-label="Two students smiling at a laptop" style="width:176px;height:176px;background:linear-gradient(160deg,#f0e6d8,#c79b4e 60%,#7a6a5a)"></div></div>

<h2 class="abs rules-title">Rules of Procedure</h2>
<svg class="abs divider" style="top:1509px" viewBox="0 0 180 16"><line x1="0" y1="8" x2="72" y2="8" stroke="#fff"/><line x1="108" y1="8" x2="180" y2="8" stroke="#fff"/><circle cx="76" cy="8" r="2.5" fill="#fff"/><circle cx="104" cy="8" r="2.5" fill="#fff"/><circle cx="90" cy="8" r="6" fill="none" stroke="#fff" stroke-width="1.5"/><circle cx="90" cy="8" r="3" fill="#fff"/></svg>

<div class="abs rule-row" style="top:1544px;left:402px">
  <svg width="42" height="50" viewBox="0 0 42 50" fill="none" stroke="#fff" stroke-width="1.6"><rect x="4" y="10" width="26" height="36"/><path d="M10 10V4h26v36h-6"/><path d="M10 18h14M10 24h14M10 30h14M10 36h14"/></svg>
  <div><p>Please find attached the rules of procedure</p><a>Rules of Procedure</a></div>
</div>
<div class="abs rule-row" style="top:1620px;left:396px">
  <svg width="48" height="48" viewBox="0 0 48 48" fill="none" stroke="#fff" stroke-width="1.6"><path d="M4 12l18 4v28L4 40z"/><path d="M44 12l-18 4v28l18-4z"/><path d="M9 22l9 2M9 28l9 2M30 24l9-2M30 30l9-2"/><path d="M24 4l8 4-8 4-8-4z"/></svg>
  <div><p>Please find attached the educational Project</p><a>Educational Project</a></div>
</div>

<!-- activities -->
<h2 class="abs sec-title" style="top:1915px">ROYAL DE VELMOQ ACTIVITIES</h2>
<svg class="abs divider" style="top:1965px" viewBox="0 0 180 16"><line x1="0" y1="8" x2="72" y2="8" stroke="#1b75bf"/><line x1="108" y1="8" x2="180" y2="8" stroke="#1b75bf"/><circle cx="76" cy="8" r="2.5" fill="#1b75bf"/><circle cx="104" cy="8" r="2.5" fill="#1b75bf"/><circle cx="90" cy="8" r="6" fill="none" stroke="#1b75bf" stroke-width="1.5"/><circle cx="90" cy="8" r="3" fill="#1b75bf"/></svg>
<p class="abs sec-text" style="top:1990px">Lorem ipsum dolor sit amet, consectetur adipiscing elit, sed do eiusmod tempor incididunt ut<br>labore et dolore magna aliqua. Quis ipsum suspendisse ultrices gravida. Risus commodo<br>viverra maecenas accumsan lacus vel facilisis.</p>

<div class="abs tile" role="img" aria-label="Students reading together in class" style="left:148px;background:linear-gradient(180deg,#6b5448 0%,#3b2c26 100%)">
  <span class="badge" style="background:var(--orange)"><svg width="20" height="20" fill="none" stroke="#fff" stroke-width="1.6"><path d="M4 16C10 10 10 10 16 4M4 4c2 6 6 10 12 12M7 10l3 3M10 7l3 3"/></svg></span>Genetics</div>
<div class="abs tile" role="img" aria-label="Group of laughing students on a trip" style="left:449px;background:linear-gradient(180deg,#8a7d5c 0%,#3e3a30 100%)">
  <span class="badge" style="background:var(--orange)"><svg width="20" height="20" fill="none" stroke="#fff" stroke-width="1.6"><rect x="3" y="7" width="14" height="7" rx="2"/><path d="M5 7l2-3h6l2 3"/><circle cx="6.5" cy="15.5" r="1.5"/><circle cx="13.5" cy="15.5" r="1.5"/></svg></span>Trips</div>
<div class="abs tile" role="img" aria-label="Students walking in front of the school building" style="left:751px;top:2088px;height:290px;background:linear-gradient(180deg,#cfd4d8 0%,#8e9479 60%,#4c5a3b 100%)">
  <span class="badge" style="background:var(--blue-dark)"><svg width="22" height="20" fill="none" stroke="#fff" stroke-width="1.6"><path d="M2 7l9-4 9 4-9 4z"/><path d="M6 9v5c3 2 7 2 10 0V9"/><path d="M20 7v6"/></svg></span>Farewell</div>

<!-- meals -->
<div class="abs meal-photo" role="img" aria-label="Colourful Mexican dishes with guacamole, tacos, peppers and lime"></div>
<div class="abs chat"><svg width="62" height="52" viewBox="0 0 62 52" fill="none" stroke="#fff" stroke-width="2"><path d="M8 4h40a6 6 0 0 1 6 6v18a6 6 0 0 1-6 6H24l-10 9v-9H8a6 6 0 0 1-6-6V10a6 6 0 0 1 6-6z" fill="#fff"/><circle cx="18" cy="19" r="3.5" fill="#d86f1a" stroke="none"/><circle cx="28" cy="19" r="3.5" fill="#d86f1a" stroke="none"/><circle cx="38" cy="19" r="3.5" fill="#d86f1a" stroke="none"/><path d="M56 16a6 6 0 0 1 4 6v14a6 6 0 0 1-6 6h-4v8l-9-8"/></svg></div>
<h2 class="abs meal-title">MEALS OFFERED</h2>
<svg class="abs divider" style="top:2629px;left:647px" viewBox="0 0 180 16"><line x1="0" y1="8" x2="72" y2="8" stroke="#1b75bf"/><line x1="108" y1="8" x2="180" y2="8" stroke="#1b75bf"/><circle cx="76" cy="8" r="2.5" fill="#1b75bf"/><circle cx="104" cy="8" r="2.5" fill="#1b75bf"/><circle cx="90" cy="8" r="6" fill="none" stroke="#1b75bf" stroke-width="1.5"/><circle cx="90" cy="8" r="3" fill="#1b75bf"/></svg>
<div class="abs meal-text">
  <p>to the students &nbsp;of the secondary section of L'ATHÉNÉE ROYAL DE VELMOQ &nbsp;during the whole school year!</p>
  <p style="margin-top:28px">Pilot project for your little ones, our little ones &nbsp;of the AR VELMOQ. Which team !</p>
</div>
<div class="abs arrow-btn" style="left:1024px;background:#e9ebee"><svg width="18" height="12"><path d="M17 6H2M7 1L2 6l5 5" fill="none" stroke="#333" stroke-width="1.5"/></svg></div>
<div class="abs arrow-btn" style="left:1072px;background:var(--blue-dark)"><svg width="18" height="12"><path d="M1 6h15M11 1l5 5-5 5" fill="none" stroke="#fff" stroke-width="1.5"/></svg></div>

<!-- contact -->
<h2 class="abs sec-title" style="top:3019px">CONTACT US</h2>
<svg class="abs divider" style="top:3069px" viewBox="0 0 180 16"><line x1="0" y1="8" x2="72" y2="8" stroke="#1b75bf"/><line x1="108" y1="8" x2="180" y2="8" stroke="#1b75bf"/><circle cx="76" cy="8" r="2.5" fill="#1b75bf"/><circle cx="104" cy="8" r="2.5" fill="#1b75bf"/><circle cx="90" cy="8" r="6" fill="none" stroke="#1b75bf" stroke-width="1.5"/><circle cx="90" cy="8" r="3" fill="#1b75bf"/></svg>

<footer class="abs footer"></footer>
<form class="abs form-card">
  <div class="abs field" style="left:46px;top:28px;width:267px">Name</div>
  <div class="abs field" style="left:334px;top:28px;width:267px">Email Address</div>
  <div class="abs field" style="left:46px;top:90px;width:267px">Phone Number</div>
  <div class="abs field" style="left:334px;top:90px;width:267px">Address</div>
  <div class="abs field msg" style="left:46px;top:154px;width:555px">Message</div>
</form>
<a class="btn-parents submit"><span>SUBSCRIBE</span></a>

<div class="abs info" style="left:131px">
  <span class="ic"><svg width="22" height="30" viewBox="0 0 22 30"><path d="M11 1C5.5 1 1 5.5 1 11c0 7.5 10 18 10 18s10-10.5 10-18C21 5.5 16.5 1 11 1z" fill="#fff"/><circle cx="11" cy="11" r="4" fill="#1466ad"/></svg></span>
  <div><h4>LOCATION:</h4><p>RUE GASTON LEMARCHE 1 / A, 4820<br>VELMOQ, BELGIUM</p></div>
</div>
<div class="abs info" style="left:531px">
  <span class="ic"><svg width="32" height="32" fill="none" stroke="#fff" stroke-width="2"><circle cx="16" cy="16" r="13"/><path d="M16 8v8l5 4"/></svg></span>
  <div><h4>SCHEDULE:</h4><p>MONDAY TO FRIDAY<br>7 AM - 6 PM</p></div>
</div>
<div class="abs info" style="left:844px">
  <span class="ic"><svg width="30" height="30" viewBox="0 0 24 24"><path d="M6.6 10.8a15.1 15.1 0 0 0 6.6 6.6l2.2-2.2c.3-.3.7-.4 1-.2 1.1.4 2.3.6 3.6.6.6 0 1 .4 1 1V20c0 .6-.4 1-1 1C10.6 21 3 13.4 3 4c0-.6.4-1 1-1h3.5c.6 0 1 .4 1 1 0 1.3.2 2.5.6 3.6.1.3 0 .7-.2 1z" fill="#fff"/></svg></span>
  <div><h4>PHONE:</h4><p>+32 81 47 36 58</p></div>
</div>
<div class="abs foot-line"></div>
<p class="abs copy">© 2019 ROYAL DE VELMOQ.ALL RIGHTS RESERVED</p>
<a class="abs sitemap">SITE MAP</a>
<a class="abs totop"><svg width="12" height="18"><path d="M6 17V2M1 7l5-5 5 5" fill="none" stroke="#fff" stroke-width="1.5"/></svg></a>

</body>
</html>
```